Tri-fold brochue, business card, and stationary design.

Tri-fold brochure: We are looking to get a tri-fold brochure template created so we can add our content on each side of the brochure and then leave these with prospective clients during sales calls.Business card: We would like the business card to have employee name, phone number, and email address on the card. We are open to rounded corners as well.We just redid our website and we'd like all designs to be complementary to our new "Look and feel" of our website.

Contact Information for Business Card

We would like the business card to have employee name, phone number, and email address on the card. We are open to rounded corners as well.

We just redid our website and we'd like all designs to be complementary to our new "Look and feel" of our website.

```html
<!DOCTYPE html>
<html lang="en">
<head>
<meta charset="utf-8">
<title>Harborline Systems — Business Card</title>
<link rel="stylesheet" href="https://fonts.googleapis.com/css2?family=Montserrat:wght@300;500;700;800&family=Roboto:wght@400&display=swap">
<style>
  :root {
    --page-bg: #ececec;
    --card-bg: #ffffff;
    --brand-cyan: #00a6da;
    --brand-blue: #0085c8;
    --brand-deep: #0063a8;
    --brand-pale: #e9f4fa;
    --ink-dark: #1b3350;
    --pattern-tone: #eef1f4;
  }
  * { margin: 0; padding: 0; box-sizing: border-box; }
  html, body {
    width: 1200px; height: 1200px; overflow: hidden;
    background: var(--page-bg);
    font-family: "Montserrat", sans-serif;
  }
  .sheet {
    width: 1200px; height: 1200px;
    display: flex; flex-direction: column; align-items: center; justify-content: center;
    gap: 44px;
  }
  .card {
    position: relative;
    width: 900px; height: 514px;
    background: var(--card-bg);
    border-radius: 6px;
    overflow: hidden;
    box-shadow: 0 10px 30px rgba(0,0,0,0.12);
  }
  .card__wave { position: absolute; inset: 0; width: 100%; height: 100%; }
  .card__pattern {
    position: absolute; top: 0; right: 0; width: 560px; height: 420px;
    background: radial-gradient(ellipse at 60% 35%, var(--pattern-tone) 0%, rgba(238,241,244,0) 70%);
  }
  /* Front */
  .brand {
    position: absolute; left: 400px; top: 150px;
    display: flex; align-items: center; gap: 22px;
  }
  .brand__dot {
    width: 62px; height: 62px; border-radius: 50%;
    background: var(--brand-blue);
  }
  .brand__name {
    font-weight: 700; font-size: 58px; line-height: 1; color: var(--brand-cyan);
    letter-spacing: -0.5px;
  }
  .brand__tag {
    display: block; font-weight: 700; font-size: 22px; color: var(--brand-cyan);
    letter-spacing: 20px; margin-top: 6px;
  }
  .web-address {
    position: absolute; left: 470px; top: 330px;
    font-weight: 500; font-size: 20px; color: var(--brand-blue); letter-spacing: 0.5px;
  }
  /* Back */
  .person { position: absolute; left: 420px; top: 80px; }
  .person__name {
    font-weight: 800; font-size: 54px; color: var(--brand-cyan); letter-spacing: 1px; line-height: 1;
  }
  .person__role {
    font-weight: 300; font-size: 34px; color: var(--brand-cyan); letter-spacing: 8px; margin-top: 6px;
  }
  .contacts {
    position: absolute; left: 470px; top: 260px;
    list-style: none; display: flex; flex-direction: column; gap: 22px;
  }
  .contacts__item {
    display: flex; align-items: center; gap: 18px;
    font-family: "Roboto", sans-serif; font-size: 24px; color: var(--ink-dark);
  }
  .contacts__icon {
    width: 46px; height: 46px; border-radius: 50%; background: var(--brand-blue);
    display: flex; align-items: center; justify-content: center; flex-shrink: 0;
  }
  .back-brand {
    position: absolute; left: 110px; top: 420px;
    font-weight: 700; font-size: 30px; color: #ffffff;
  }
</style>
</head>
<body>
<main class="sheet">

  <section class="card card--front" aria-label="Card front">
    <div class="card__pattern" role="img" aria-label="Faint network line pattern"></div>
    <svg class="card__wave" viewBox="0 0 900 514" preserveAspectRatio="none" aria-hidden="true">
      <defs>
        <linearGradient id="waveFront" x1="0" y1="0" x2="1" y2="1">
          <stop offset="0" stop-color="#00aadd"/>
          <stop offset="1" stop-color="#0072b8"/>
        </linearGradient>
      </defs>
      <path d="M0,150 C90,150 120,300 300,360 C420,400 520,400 620,514 L0,514 Z" fill="var(--brand-deep)"/>
      <path d="M0,200 C110,190 160,330 330,390 C440,430 500,440 560,514 L0,514 Z" fill="url(#waveFront)"/>
      <path d="M0,210 C40,200 70,230 100,290 C60,270 30,260 0,262 Z" fill="var(--brand-cyan)" opacity="0.7"/>
    </svg>
    <div class="brand">
      <span class="brand__dot"></span>
      <div>
        <span class="brand__name">Harborline</span>
        <span class="brand__tag">Systems</span>
      </div>
    </div>
    <p class="web-address">WWW.HARBORLINESYSTEMS.COM</p>
  </section>

  <section class="card card--back" aria-label="Card back">
    <svg class="card__wave" viewBox="0 0 900 514" preserveAspectRatio="none" aria-hidden="true">
      <defs>
        <linearGradient id="waveBack" x1="0" y1="0" x2="1" y2="1">
          <stop offset="0" stop-color="#00aadd"/>
          <stop offset="1" stop-color="#0072b8"/>
        </linearGradient>
      </defs>
      <path d="M0,210 C90,200 130,330 320,390 C440,420 540,420 640,514 L0,514 Z" fill="var(--brand-deep)"/>
      <path d="M0,250 C110,240 160,360 340,410 C450,440 510,460 570,514 L0,514 Z" fill="url(#waveBack)"/>
    </svg>
    <div class="person">
      <h1 class="person__name">YOUR NAME</h1>
      <p class="person__role">your position</p>
    </div>
    <ul class="contacts">
      <li class="contacts__item">
        <span class="contacts__icon">
          <svg width="24" height="18" viewBox="0 0 24 18" aria-hidden="true">
            <rect x="1" y="1" width="22" height="16" rx="1" fill="none" stroke="#fff" stroke-width="2"/>
            <path d="M1,2 L12,10 L23,2" fill="none" stroke="#fff" stroke-width="2"/>
          </svg>
        </span>
        youremail@company.com
      </li>
      <li class="contacts__item">
        <span class="contacts__icon">
          <svg width="24" height="24" viewBox="0 0 24 24" aria-hidden="true">
            <path d="M6.6 10.8a15 15 0 0 0 6.6 6.6l2.2-2.2a1 1 0 0 1 1-.25 11.4 11.4 0 0 0 3.6.57 1 1 0 0 1 1 1V20a1 1 0 0 1-1 1A17 17 0 0 1 3 4a1 1 0 0 1 1-1h3.5a1 1 0 0 1 1 1c0 1.25.2 2.45.57 3.6a1 1 0 0 1-.25 1z" fill="#fff"/>
          </svg>
        </span>
        + 0 000 . 0000
      </li>
    </ul>
    <p class="back-brand">Harborline</p>
  </section>

</main>
</body>
</html>
```